Disposable Mini Sauce Pot Design for Asian Chain Food Brands

We operate a Hainan Chicken Rice takeout brand under the name Wokly8, with our official website: www.Wokly8.com.
We offer four signature house sauces and are launching brand-new packaging for our sauce line. We require custom graphic designs exclusively for the sauce cup lids.
Product Material & Base Specs
The sauce cups are made of PP plastic, available in two translucent base options: Translucent White and Translucent Orange.
Four Sauce Varieties for Individual Lid Designs
1. Red Sauce – Fried Sweet Chili Sauce
2.Green Sauce – Scallion Oil Dressing
3.Sweet Soy Sauce
4.Sweet Red Sauce (Special for Fried Chicken)
Differentiate each sauce lid design through unique graphics, typography, or illustrative elements for easy customer identification.
The marking NET WT 2 OZ must be clearly printed on every lid.
**There is no need to print full descriptive text or the full name of the sauces on each lid; the design only needs to clearly differentiate the four sauce varieties.
**Please reference the original design style and brand color palette shown on our official website, and feel free to fully unleash your creativity.
Look and feel
Each slider illustrates characteristics of the customer's brand and the style your logo design should communicate.

```html
<!DOCTYPE html>
<html lang="en">
<head>
<meta charset="utf-8">
<title>Wokly8 Sauce Lids</title>
<link rel="stylesheet" href="https://fonts.googleapis.com/css2?family=Oswald:wght@500;700&display=swap">
<style>
  :root {
    --bg: #0f0f10;
    --paper: #f6f3ee;
    --brand-orange: #e8611c;
    --red: #d3191f;
    --green: #3f7a26;
    --soy: #2e1d13;
    --soy-rim: #4b3326;
    --sweet-red: #ee6b1c;
    --chili-fill: linear-gradient(135deg, #e0282b, #b8141a);
    --scallion-fill: linear-gradient(135deg, #6aa336, #2f6a1f);
    --soy-fill: linear-gradient(135deg, #5a3a27, #24160e);
    --splash-fill: linear-gradient(135deg, #f58a2c, #e2511a);
  }
  * { box-sizing: border-box; margin: 0; padding: 0; }
  html, body { width: 1200px; height: 800px; overflow: hidden; }
  body {
    background: var(--bg);
    font-family: "Oswald", "Arial Narrow", sans-serif;
    display: flex;
    align-items: center;
    justify-content: center;
  }
  .lid-row { display: flex; gap: 20px; }
  .lid {
    width: 270px; height: 270px;
    border-radius: 36px;
    padding: 12px;
    background: var(--rim);
  }
  .lid--red { --rim: var(--red); --ink: var(--red); --art: var(--chili-fill); }
  .lid--green { --rim: var(--green); --ink: var(--green); --art: var(--scallion-fill); }
  .lid--soy { --rim: var(--soy-rim); --ink: var(--soy); --art: var(--soy-fill); }
  .lid--sweet-red { --rim: var(--sweet-red); --ink: var(--sweet-red); --art: var(--splash-fill); }
  .lid-face {
    position: relative;
    width: 100%; height: 100%;
    border-radius: 26px;
    background: var(--paper);
    padding: 16px 12px 14px 18px;
  }
  .brand { color: var(--brand-orange); }
  .brand-name { font-weight: 700; font-size: 24px; line-height: 1; letter-spacing: .5px; }
  .brand-tag { font-weight: 500; font-size: 7px; letter-spacing: .6px; margin-top: 2px; }
  .sauce-name {
    position: absolute; left: 18px; top: 70px; z-index: 1;
    color: var(--ink); font-weight: 700; line-height: .92;
    text-transform: uppercase; white-space: nowrap;
  }
  .sauce-name span { display: block; }
  .sauce-name .big { font-size: 58px; }
  .sauce-name .big--long { font-size: 48px; }
  .sauce-name .mid { font-size: 40px; }
  .sauce-name .small { font-size: 30px; }
  .sauce-art {
    position: absolute; right: 12px; top: 70px;
    width: 70px; height: 112px;
    border-radius: 34px 8px 34px 8px;
    background: var(--art);
  }
  .net-wt {
    position: absolute; left: 18px; bottom: 14px;
    font-weight: 500; font-size: 12px; color: var(--ink);
  }
</style>
</head>
<body>
  <main class="lid-row">
    <section class="lid lid--red">
      <div class="lid-face">
        <div class="brand"><div class="brand-name">Wokly8</div><div class="brand-tag">HAINAN CHICKEN</div></div>
        <h2 class="sauce-name"><span class="big">Red</span><span class="mid">Sauce</span></h2>
        <div class="sauce-art" role="img" aria-label="Illustration of a red chili pepper"></div>
        <p class="net-wt">NET WT 2 OZ</p>
      </div>
    </section>
    <section class="lid lid--green">
      <div class="lid-face">
        <div class="brand"><div class="brand-name">Wokly8</div><div class="brand-tag">HAINAN CHICKEN</div></div>
        <h2 class="sauce-name"><span class="big big--long">Green</span><span class="mid">Sauce</span></h2>
        <div class="sauce-art" role="img" aria-label="Illustration of scallion stalks with sliced rings"></div>
        <p class="net-wt">NET WT 2 OZ</p>
      </div>
    </section>
    <section class="lid lid--soy">
      <div class="lid-face">
        <div class="brand"><div class="brand-name">Wokly8</div><div class="brand-tag">HAINAN CHICKEN</div></div>
        <h2 class="sauce-name"><span class="mid">Sweet</span><span class="mid">Soy</span><span class="small">Sauce</span></h2>
        <div class="sauce-art" role="img" aria-label="Illustration of a bowl of soy sauce with a drip and soybeans"></div>
        <p class="net-wt">NET WT 2 OZ</p>
      </div>
    </section>
    <section class="lid lid--sweet-red">
      <div class="lid-face">
        <div class="brand"><div class="brand-name">Wokly8</div><div class="brand-tag">HAINAN CHICKEN</div></div>
        <h2 class="sauce-name"><span class="mid">Sweet</span><span class="mid">Red</span><span class="small">Sauce</span></h2>
        <div class="sauce-art" role="img" aria-label="Illustration of a swirling orange-red sauce splash"></div>
        <p class="net-wt">NET WT 2 OZ</p>
      </div>
    </section>
  </main>
</body>
</html>
```